Velmira Construction Company Catalogue Design Project

looking for construction company catalog design, elegant, modern and shick

i made the project guaranteed for payment, waiting for serious designers. 

Reason: just made the project payment guaranteed/ so i am extending the deadline for another week.

Target Market(s)

ages 35 to 70 married couples

Industry/Entity Type

Construction

Requirements
Must have
• it should not look tacky with bunch of colors with cheesy layouts.

modern elegant shick page layout, construction company catalog showing company info and previous reference projects.

the catalog will be bound to 8.5x11" letter paper (or A4 europe)

the company info can be reached at http://www.velmira-build.example/English/

```html
<!DOCTYPE html>
<html lang="en">
<head>
<meta charset="utf-8">
<title>Velmira Construction Company – Catalogue Covers</title>
<link rel="stylesheet" href="https://fonts.googleapis.com/css2?family=Michroma&family=Oswald:wght@300&family=Roboto:wght@300;400&display=swap">
<style>
  :root {
    --backdrop: #3a3a3a;
    --paper-light: #ffffff;
    --paper-mid: #e6e6e7;
    --paper-edge: #c9c9cb;
    --ink-dark: #1d1d1f;
    --ink-grey: #6b6b6e;
    --ink-soft: #a9a9ad;
    --accent-red: #a3343a;
    --sketch-tone: #d6d8e4;
  }
  * { margin: 0; padding: 0; box-sizing: border-box; }
  html, body { width: 1200px; height: 1000px; overflow: hidden; }
  body { background: var(--backdrop); position: relative; font-family: "Roboto", Arial, sans-serif; }

  .cover {
    position: absolute;
    background: radial-gradient(circle at 50% 24%, var(--paper-light) 0%, var(--paper-mid) 62%, var(--paper-edge) 100%);
    overflow: hidden;
  }
  .cover--back { left: 148px; top: 78px; width: 502px; height: 712px; }
  .cover--front { left: 522px; top: 170px; width: 502px; height: 710px; border-left: 2px solid #9a9a9d; }

  .brand-name {
    font-family: "Michroma", "Arial Black", sans-serif;
    color: var(--ink-dark);
    letter-spacing: 1px;
    line-height: 1;
    white-space: nowrap;
  }
  .brand-tagline {
    font-family: "Roboto", Arial, sans-serif;
    color: var(--ink-grey);
    text-transform: uppercase;
    white-space: nowrap;
  }

  /* back cover */
  .back-brand { position: absolute; left: 152px; top: 496px; display: flex; align-items: center; gap: 10px; }
  .back-brand .brand-mark { width: 26px; height: 26px; border-radius: 50%; background: var(--ink-dark); }
  .back-brand .brand-name { font-size: 21px; }
  .back-brand .brand-tagline { position: absolute; left: 36px; top: 28px; font-size: 7px; letter-spacing: 1.3px; }
  .back-contact {
    position: absolute; left: 150px; top: 570px; width: 200px;
    text-align: center; font-size: 9.5px; line-height: 12px; color: var(--ink-soft); font-weight: 300;
  }
  .back-contact .company { margin-bottom: 12px; }

  /* front cover */
  .front-brand { position: absolute; left: 0; top: 192px; width: 100%; text-align: center; }
  .front-brand .brand-name { font-size: 24px; }
  .front-brand .brand-tagline { margin-top: 4px; font-size: 7.5px; letter-spacing: 1.6px; }

  .house-sketch {
    position: absolute; left: 40px; top: 390px; width: 462px; height: 320px;
    background: linear-gradient(160deg, rgba(214,216,228,0) 0%, var(--sketch-tone) 55%, rgba(214,216,228,0.6) 100%);
    clip-path: polygon(35% 30%, 55% 0%, 75% 8%, 100% 25%, 100% 100%, 0% 100%, 0% 55%, 18% 45%);
  }

  .catalog-tag {
    position: absolute; left: 260px; top: 575px; width: 242px; height: 45px;
    background: var(--accent-red); border-radius: 23px 0 0 23px;
    display: flex; align-items: center; justify-content: center;
    font-family: "Oswald", "Arial Narrow", sans-serif; font-weight: 300;
    font-size: 27px; letter-spacing: 1px; color: #fff;
  }
</style>
</head>
<body>
  <section class="cover cover--back" aria-label="Catalogue back cover">
    <div class="back-brand">
      <span class="brand-mark"></span>
      <span class="brand-name">VELMIRA</span>
      <span class="brand-tagline">Yapı Mühendislik San. Tic. Ltd.</span>
    </div>
    <address class="back-contact" style="font-style:normal">
      <p class="company">Velmira Yapı Mühendislik Ltd.</p>
      <p>Phone : 0(216) 555 01 20 -</p>
      <p>Fax : 0(216) 555 01 30</p>
      <p>Linden Plaza B-2 Blok</p>
      <p>No:14 Kadıköy/İSTANBUL</p>
    </address>
  </section>

  <section class="cover cover--front" aria-label="Catalogue front cover">
    <div class="front-brand">
      <div class="brand-name">VELMIRA</div>
      <div class="brand-tagline">Construction &amp; Engineering</div>
    </div>
    <div class="house-sketch" role="img" aria-label="Faint architectural line sketch of a pitched-roof house"></div>
    <div class="catalog-tag">CATALOG</div>
  </section>
</body>
</html>
```